Cruise Booking Website

Cruise search and booking website

This project is a redesign of a cruise booking website we did a few years ago.

The current website is located here: http://voyage.pixelmarsh.com/en/

It's not fully functional but gives you ad idea how miserable the old design was.

All the information about cruises, cruise lines, destinations, ports and shore excursions will be similar to http://www.sailorbay.com/
Actual search pages (form, results, single result, sailing and cabin selection, ship info, booking) will have EXACTLY the same info as sailorbay.com

We like the style of http://harborvoyagehub.com, it's quite modern, good spacing, not overloaded with information. So you can use it as an example of what we like, not what we want as a final result for us. Please, don't copy it. The result should not be possible to resemble the harborvoyagehub.com, because our site has to be unique. This is important!
If you submit a design that clearly reminds another cruise site it will be rejected!

Also the mockup provided is just to give you the basic structure and show what information has to be present on the page. It doesn't mean the layout has to be the same as a mockup. The layout is up to the designer.

I've updated the mockup to be more generic so it doesn't confuse you:
https://www.filecrate.net/s/k7q2mz9pw4tnb3x/Home%20page.png

When you're adding social sharing icons like chatterbox/peeplet you have to use chinese ones instead:
https://www.filecrate.net/s/h3rt8wyd6jcl0fe/chinese-social-icons.png
Originals: http://shrtlk.example/qRmT

We'll start with home page first and after it's approved inner pages can be designed.

I know the cost of the project doesn't look high, but the task is straight forward and doesn't require to be very original, it's better to follow existing design and layout patterns that proved to work well.
That's why I encourage you to choose a template to build the design on top of one of https://themequarry.net/ themes if it will save the design work, will be easier and faster for you. So it will be more like a customization than a new design from scratch.

Mockups, site map and logo files:
- https://www.filecrate.net/sh/50xb7vq1ndtpkez/RmwuHp8Zq3

Website tree:
- https://papers.quillnet.example/document/d/8vTrXk2MqLpZ4wNsB7yHcE1oUjFgD9aR_QbVtnWm/edit?usp=sharing
Updates

So far a lot of designs are just copying http://www.harborvoyagehub.com/ - we don't like it!

We like the style of harborvoyagehub.com, it's quite modern, good spacing, not overloaded with information. So you can use it as an example of what we like, not what we want as a final result for us. Please, don't copy it. The result should not be possible to resemble the harborvoyagehub.com, because our site has to be unique. This is important!

Target Market(s)

Chinese travellers

Industry/Entity Type

Build

Requirements
Must have
• * White, blue and red
* Large spacing, not too much information cramped into a small space like sailorbay.com or the current website
* More "hidden" info in popups, tabs and so on, so not to many things are visible at the same time
* Compatible with lumen framekit styling (for easier coding):
- http://lumenkit.example.io/framework/index.html
- http://skinvault.net/
* Feel free to propose to build the design on top of one of https://themequarry.net/ themes if it will save the design work, will be easier and faster for you

```html
<!DOCTYPE html>
<html lang="en">
<head>
<meta charset="utf-8">
<title>BlueWake Cruises – About Us</title>
<link href="https://fonts.googleapis.com/css2?family=Oswald:wght@300;400;500&family=Open+Sans:wght@400;600;700&display=swap" rel="stylesheet">
<style>
:root{
  --navy:#174d83;
  --blue:#2376bd;
  --sky:#5fb2e6;
  --pale:#d8e8f6;
  --field:#e6f1fb;
  --red:#e1262d;
  --white:#ffffff;
  --ink:#1e3b5a;
  --foot:#1a4f86;
  --foot-dark:#123c68;
}
*{box-sizing:border-box;margin:0;padding:0}
html,body{width:788px;height:1200px;overflow:hidden}
body{position:relative;font-family:"Open Sans",Arial,sans-serif;color:var(--ink);background:#eaf4fb}
.scene{position:absolute;left:0;top:0;width:788px;height:880px;background:linear-gradient(180deg,#4aa6df 0%,#8fd0f2 18%,#c9ebf9 40%,#6fc4e6 62%,#e9e0c6 100%)}
.abs{position:absolute}
.logo{left:18px;top:26px;display:flex;align-items:center;gap:8px}
.logo-dot{width:30px;height:30px;border-radius:50%;background:var(--white)}
.logo-name{font:600 22px "Open Sans",sans-serif;color:var(--white)}
.account{left:468px;top:8px;display:flex;gap:4px}
.account span{background:var(--white);color:var(--blue);font-size:10px;padding:3px 12px;border-radius:3px 3px 0 0}
.hotline-top{left:618px;top:6px;display:flex;align-items:center;gap:6px;color:var(--white);font:500 22px "Oswald",sans-serif}
.hotline-top .icon{width:24px;height:24px;border-radius:50%;background:var(--white);display:flex;align-items:center;justify-content:center}
.nav{left:225px;top:50px;display:flex;gap:30px}
.nav-item{width:46px;height:46px;border-radius:50%;background:var(--navy);border:3px solid var(--white);display:flex;align-items:center;justify-content:center;box-shadow:0 2px 4px rgba(0,0,0,.25)}
.panel-title{font:300 21px "Oswald",sans-serif;color:var(--white);letter-spacing:.5px}
.search{left:20px;top:118px;width:242px;height:277px;background:linear-gradient(180deg,#1f64a6,#174d83);padding:12px 18px;border-radius:3px}
.select{height:22px;margin-top:7px;background:var(--field);border-radius:2px;font-size:10px;color:var(--ink);padding:4px 8px;display:flex;justify-content:space-between;text-transform:uppercase}
.select::after{content:"▾"}
.travel-label{font:300 17px "Oswald",sans-serif;color:var(--white);margin-top:12px}
.pair{display:flex;gap:8px}
.pair .select{flex:1}
.btn-search{margin:22px auto 0;width:150px;height:26px;border-radius:13px;background:var(--sky);color:var(--white);font-size:11px;display:flex;align-items:center;justify-content:center}
.newsletter{left:20px;top:420px;width:242px;height:145px;background:var(--white);border-radius:3px;padding:10px 14px}
.newsletter h3{font:400 14px "Oswald",sans-serif;color:var(--navy);border-bottom:1px solid var(--pale);padding-bottom:6px}
.newsletter p{font-size:9px;margin-top:6px;color:#5b7590}
.newsletter .input{margin-top:6px;height:22px;border:1px solid #b8cfe4;font-size:9px;color:#8aa0b5;padding:5px 6px}
.btn-red{display:inline-block;margin-top:8px;background:var(--red);color:var(--white);font-size:10px;padding:5px 12px;border-radius:2px}
.promo{left:20px;top:585px;width:242px;height:205px;background:var(--white);border-radius:3px;padding:8px}
.promo h3{font:500 22px "Oswald",sans-serif;color:var(--red);padding:0 4px}
.promo .art{margin-top:4px;height:152px;background:linear-gradient(160deg,#52b6e6,#e9f4fb 55%,#e8485a)}
.main{left:270px;top:118px;width:498px;height:682px;background:var(--pale);border:1px solid #b8d3ea;border-radius:3px;padding:10px 20px}
.crumb{background:var(--white);font-size:10px;padding:5px 8px;color:#5b7590}
.crumb b{color:var(--blue);font-weight:600}
.main h1{font:400 27px "Oswald",sans-serif;color:var(--blue);margin-top:8px}
.main p{font-size:9.5px;line-height:1.45;color:#4d6a86;margin-top:6px}
.video{margin-top:14px;height:214px;position:relative;background:linear-gradient(180deg,#a9d7f0 0%,#5fa9d8 55%,#1e5f95 100%)}
.video .bar{position:absolute;left:0;right:0;bottom:0;height:18px;background:rgba(0,0,0,.7);display:flex;align-items:center;gap:8px;padding:0 8px}
.video .track{flex:1;height:3px;background:#8b8b8b}
.brands{left:0;top:815px;width:788px;height:55px;background:var(--white);display:flex;align-items:center;justify-content:space-between;padding:0 22px}
.brands .arrow{color:var(--blue);font-size:18px}
.brands .name{font:600 12px "Open Sans",sans-serif;color:var(--navy)}
.footer{left:0;top:880px;width:788px;height:280px;background:var(--foot);padding:18px 20px;display:flex;gap:34px;color:var(--white)}
.footer h2{font:400 21px "Oswald",sans-serif;margin-bottom:8px}
.col-links{width:220px}
.col-links li{list-style:none;font-size:10.5px;line-height:1.45}
.btn-small{display:inline-block;margin-top:6px;font-size:9px;background:var(--blue);padding:3px 8px;border-radius:2px}
.col-mail{width:270px}
.field{display:flex;align-items:center;gap:8px;margin-bottom:6px;font-size:10px}
.field span{width:46px}
.field i{flex:1;height:18px;background:var(--field);display:block}
.area{height:58px;background:var(--field);margin-left:54px}
.btn-send{margin:8px 0 0 180px;display:inline-block;background:var(--blue);font-size:10px;padding:4px 14px;border-radius:2px}
.col-contact{width:190px;font-size:10px;line-height:1.5}
.social{display:flex;gap:6px;margin:8px 0}
.social i{width:20px;height:20px;border-radius:50%;background:var(--sky);display:block}
.hotline{font:400 20px "Oswald",sans-serif}
.bottom{left:0;top:1160px;width:788px;height:40px;background:var(--foot-dark);color:#cfe0f0;font-size:9.5px;text-align:center;padding-top:6px;line-height:1.5}
</style>
</head>
<body>
<div class="scene" role="img" aria-label="Bright sky, sea and beach background scene"></div>

<div class="abs logo"><span class="logo-dot"></span><span class="logo-name">BlueWake</span></div>
<div class="abs account"><span>sign in</span><span>sign up</span></div>
<div class="abs hotline-top">
  <span class="icon"><svg width="14" height="14" viewBox="0 0 24 24"><path d="M6.6 10.8a15 15 0 006.6 6.6l2.2-2.2a1 1 0 011-.25 11 11 0 003.5.56 1 1 0 011 1V20a1 1 0 01-1 1A17 17 0 013 4a1 1 0 011-1h3.5a1 1 0 011 1 11 11 0 00.56 3.5 1 1 0 01-.25 1z" fill="#2376bd"/></svg></span>
  4008 512 930
</div>

<nav class="abs nav">
  <span class="nav-item"><svg width="20" height="20" viewBox="0 0 24 24"><path d="M3 11l9-8 9 8v10h-6v-6H9v6H3z" fill="#fff"/></svg></span>
  <span class="nav-item"><svg width="20" height="20" viewBox="0 0 24 24"><path d="M12 2a7 7 0 017 7c0 5-7 13-7 13S5 14 5 9a7 7 0 017-7zm0 4a3 3 0 100 6 3 3 0 000-6z" fill="#fff"/></svg></span>
  <span class="nav-item"><svg width="20" height="20" viewBox="0 0 24 24"><path d="M2 15h20l-3 5H5zM6 14V9h12v5zM9 8V5h6v3z" fill="#fff"/></svg></span>
  <span class="nav-item"><svg width="20" height="20" viewBox="0 0 24 24"><rect x="3" y="5" width="18" height="16" rx="2" fill="none" stroke="#fff" stroke-width="2"/><path d="M3 10h18M8 3v4M16 3v4" stroke="#fff" stroke-width="2"/></svg></span>
  <span class="nav-item"><svg width="20" height="20" viewBox="0 0 24 24"><circle cx="12" cy="5" r="2.5" fill="none" stroke="#fff" stroke-width="2"/><path d="M12 7v14M5 13a7 7 0 0014 0M8 11h8" stroke="#fff" stroke-width="2" fill="none"/></svg></span>
  <span class="nav-item"><svg width="20" height="20" viewBox="0 0 24 24"><path d="M12 3l2.8 5.8 6.2.9-4.5 4.4 1 6.2L12 17.3l-5.5 3 1-6.2L3 9.7l6.2-.9z" fill="#fff"/></svg></span>
  <span class="nav-item"><svg width="20" height="20" viewBox="0 0 24 24"><path d="M4 5h16v11H9l-5 4z" fill="#fff"/></svg></span>
</nav>

<aside class="abs search">
  <div class="panel-title">SEARCH CRUISE</div>
  <div class="select">Destination</div>
  <div class="select">Month</div>
  <div class="select">Length</div>
  <div class="select">Cruise Line</div>
  <div class="travel-label">number of travelers</div>
  <div class="pair"><div class="select">Age 25+</div><div class="select">Age 3-18</div></div>
  <div class="btn-search">search for cruises</div>
</aside>

<section class="abs newsletter">
  <h3>CRUISE DEALS NEWSLETTER</h3>
  <p>Subscribe and get the best cruise deals now</p>
  <div class="input">Enter email address</div>
  <span class="btn-red">SUBSCRIBE</span>
</section>

<section class="abs promo">
  <h3>HOT PROMO!</h3>
  <div class="art" role="img" aria-label="Promotional banner: 40% off cruise sale with ship and beach"></div>
</section>

<main class="abs main">
  <div class="crumb"><b>Home</b> » About Us</div>
  <h1>ABOUT US</h1>
  <p>We plan cruise holidays for travellers who want calm seas, good food and easy booking. Our team compares sailings, cabins and ports across many lines, so you can choose the right ship, route and date without stress. Every trip is checked by people who have sailed them and know the small details.</p>
  <div class="video" role="img" aria-label="Video of a cruise ship sailing on open sea">
    <div class="bar">
      <svg width="10" height="10" viewBox="0 0 10 10"><path d="M1 0l8 5-8 5z" fill="#fff"/></svg>
      <span class="track"></span>
      <svg width="12" height="10" viewBox="0 0 12 10"><path d="M0 3h3l4-3v10L3 7H0z" fill="#fff"/></svg>
    </div>
  </div>
  <p>From short island escapes to long ocean voyages, we help families, couples and groups find a sailing that fits their time and budget. Our advisors speak your language and stay with you before, during and after your trip. We offer clear prices, flexible payment, shore excursions and visa help for many ports. Ask us anything, anytime, and we will reply quickly with honest advice and the best current offers.</p>
</main>

<div class="abs brands">
  <span class="arrow">◀</span>
  <span class="name">Northwind</span>
  <span class="name">Marisol</span>
  <span class="name">Stellaris</span>
  <span class="name">Corallo</span>
  <span class="name">Harrowby</span>
  <span class="name">Pinefold</span>
  <span class="name">Lowland Line</span>
  <span class="arrow">▶</span>
</div>

<footer class="abs footer">
  <div class="col-links">
    <h2>ALL ABOUT CRUISING</h2>
    <ul>
      <li>Frequently Asked Questions</li>
      <li>First Time Cruisers</li>
      <li>Value Comparison</li>
      <li>Cruising with Kids</li>
      <li>Vacation Packing Guide</li>
      <li>Onboard Activities</li>
      <li>Theme Cruises</li>
      <li>Special Event Cruises</li>
    </ul>
    <span class="btn-small">▸ See All About Cruising</span>
  </div>
  <div class="col-mail">
    <h2>SEND US AN EMAIL</h2>
    <div class="field"><span>Name</span><i></i></div>
    <div class="field"><span>Email</span><i></i></div>
    <div class="area"></div>
    <span class="btn-send">send</span>
  </div>
  <div class="col-contact">
    <h2>CONTACT US</h2>
    Book online or call<br>9:00AM - 6:00PM<br>Monday to Friday
    <div class="social"><i></i><i></i><i></i><i></i></div>
    <div class="hotline">HOTLINE: 4008 512 930</div>
  </div>
</footer>

<div class="abs bottom">
  About us | Contact us | Terms of Service | Payment info | Reward Points<br>
  Copyright © 2013 BlueWake Tours. All rights reserved.
</div>
</body>
</html>
```